Brightnest Stays Stationery Design

Letterpaper, business cards, notebook, envelope A4 & A5

Target Market(s)

Business, accommodation, hotels, flexible housing

Font styles to use
Other font styles liked:
• Montserrat

Colors

Designer to choose only greyscale colors for use in the design.

Requirements
Must have
• Luxurious appearance
Keep it simple, just like the logo
Modern
Nice to have
• Tight Luxury Design
Should not have
• Illustrations
Decorative

```html
<!DOCTYPE html>
<html lang="en">
<head>
<meta charset="utf-8">
<title>Brightnest Stays Stationery</title>
<link href="https://fonts.googleapis.com/css2?family=Montserrat:wght@400;500;600&family=Roboto:wght@400&display=swap" rel="stylesheet">
<style>
  :root{
    --board:#7d7d7d;
    --ink:#231f20;
    --paper:#f6f6f6;
    --paper-white:#ffffff;
    --text:#3a3a3a;
    --muted:#8a8a8a;
    --rule:#dcdcdc;
    --ghost:#e6e6e6;
    --label:#f2f2f2;
  }
  *{box-sizing:border-box;margin:0;padding:0}
  html,body{width:1200px;height:1030px;overflow:hidden}
  body{background:var(--board);position:relative;font-family:"Montserrat",sans-serif;color:var(--text)}
  .piece{position:absolute;background:var(--paper);overflow:hidden}
  .label{position:absolute;font-family:"Roboto",sans-serif;font-size:11px;color:var(--label);transform:translateX(-50%);white-space:nowrap}

  /* wordmark */
  .mark{position:absolute;display:flex;flex-direction:column;align-items:center;transform:translateX(-50%)}
  .mark-square{border:1.4px solid var(--ink)}
  .mark-name{font-weight:500;letter-spacing:.08em;color:var(--ink);white-space:nowrap;text-transform:uppercase}
  .mark.on-dark .mark-square{border-color:#fff}
  .mark.on-dark .mark-name{color:#fff}

  /* footer band */
  .band{position:absolute;left:0;right:0;height:11px;background:var(--ink);color:#fff;font-size:5px;letter-spacing:.2em;line-height:11px}
  .band .url{position:absolute;top:0}
  .band .chip{position:absolute;top:2px;width:8px;height:8px;border:1px solid #fff}

  .ghost-word{position:absolute;color:var(--ghost);font-weight:500;letter-spacing:.06em;white-space:nowrap;text-transform:uppercase}

  .contact{position:absolute;font-size:4.4px;line-height:6px;color:var(--muted);border-left:.6px solid var(--text);padding-left:5px}
  .contact .row{display:flex;align-items:center;gap:2px}
  .icon{width:4px;height:4px;fill:var(--text)}

  /* business card */
  .card{width:226px;height:129px}
  .card-front{left:56px;top:209px;background:var(--paper-white)}
  .card-front .person{position:absolute;left:116px;top:33px;color:var(--ink)}
  .person .name{font-size:7px;font-weight:500;letter-spacing:.03em}
  .person .role{font-size:4.6px;font-weight:600;margin-top:1px}
  .person .addr{font-size:4.6px;line-height:5.6px;margin-top:7px}
  .person .lines{font-size:4.6px;line-height:6.2px;margin-top:6px}
  .person .row{display:flex;align-items:center;gap:3px}
  .card-back{left:56px;top:367px;background:var(--ink)}
  .card-back .web{position:absolute;left:0;right:0;top:113px;text-align:center;color:#fff;font-size:5.4px;letter-spacing:.38em}

  /* letterhead */
  .letterhead{left:326px;top:50px;width:315px;height:444px;background:var(--paper)}
  .letter{position:absolute;left:33px;top:134px;width:252px;font-size:4px;line-height:6.4px;color:var(--muted)}
  .letter .greeting{font-size:7px;color:var(--text);margin-bottom:14px}
  .letter p{margin-bottom:6px}
  .letter .closing{margin-top:12px}
  .signature{position:absolute;left:31px;top:310px;width:54px;height:24px;border-radius:10px;background:linear-gradient(90deg,#dce6f2,#eef2f8)}

  /* notepads */
  .pad-large{left:682px;top:51px;width:289px;height:444px}
  .spiral-side{position:absolute;left:0;top:0;bottom:0;width:8px;background:repeating-linear-gradient(180deg,#2b2b2b 0 2px,#d8d8d8 2px 4px)}
  .ruled{position:absolute;background:repeating-linear-gradient(180deg,transparent 0 14.6px,var(--rule) 14.6px 15.6px)}
  .pad-large .ruled{left:31px;top:110px;width:233px;height:300px}
  .pad-small-cover{left:1007px;top:51px;width:145px;height:216px;background:var(--ink)}
  .pad-small-cover .web{position:absolute;left:0;right:0;top:199px;text-align:center;color:#fff;font-size:5px;letter-spacing:.12em;font-weight:500}
  .pad-small{left:1006px;top:280px;width:145px;height:216px}
  .spiral-top{position:absolute;left:0;right:0;top:0;height:4px;background:repeating-linear-gradient(90deg,#2b2b2b 0 1.5px,#cfcfcf 1.5px 3px)}
  .pad-small .ruled{left:14px;top:31px;width:118px;height:152px;background:repeating-linear-gradient(180deg,transparent 0 8.5px,var(--rule) 8.5px 9.5px)}
  .pad-small .web{position:absolute;left:0;right:0;top:197px;text-align:center;font-size:5px;letter-spacing:.12em;color:var(--muted)}

  /* envelopes */
  .env-back{left:56px;top:543px;width:434px;height:196px}
  .env-back .flap{position:absolute;left:0;top:0;width:434px;height:60px;background:var(--ink);border-radius:0 0 26px 26px;box-shadow:0 5px 6px rgba(0,0,0,.3)}
  .env-front{left:56px;top:769px;width:435px;height:199px;background:linear-gradient(90deg,#f4f4f4,#fbfbfb)}
  .address{position:absolute;font-size:7.2px;line-height:10px;color:#555}
  .env-tall{height:422px;background:transparent}
  .env-tall .body{position:absolute;left:0;right:0;top:38px;bottom:0;background:var(--paper)}
  .env-tall svg.flap{position:absolute;left:0;top:0}
  .env-a4{left:527px;top:543px;width:288px}
  .env-a5{left:857px;top:544px;width:295px}
</style>
</head>
<body>
<svg width="0" height="0" style="position:absolute">
  <symbol id="i-phone" viewBox="0 0 10 10"><path d="M2 0.5l2 2-1 1.5c.8 1.5 1.6 2.3 3 3l1.5-1 2 2-1.5 2C4 9.5.5 6 .5 2z"/></symbol>
  <symbol id="i-mobile" viewBox="0 0 10 10"><path d="M2.5 0h5v10h-5zM3.5 1v7h3V1z"/></symbol>
  <symbol id="i-fax" viewBox="0 0 10 10"><path d="M2.5 0h5v3h-5zM0 3.5h10V8H0zM2.5 8.5h5V10h-5z"/></symbol>
  <symbol id="i-mail" viewBox="0 0 10 10"><path d="M0 2h10v6H0zM1 3l4 2.6L9 3"/></symbol>
</svg>

<!-- Business card front -->
<section class="piece card card-front">
  <div class="mark" style="left:71px;top:38px">
    <div class="mark-square" style="width:28px;height:28px;margin-bottom:10px"></div>
    <div class="mark-name" style="font-size:6.6px">Brightnest Stays</div>
  </div>
  <div class="person">
    <div class="name">DANIEL REYES</div>
    <div class="role">President</div>
    <div class="addr">2140 Alder Crest Road<br>Juneau, Alaska 99801</div>
    <div class="lines">
      <div class="row"><svg class="icon"><use href="#i-phone"/></svg>555-210-4830</div>
      <div class="row"><svg class="icon"><use href="#i-mobile"/></svg>555-314-7729</div>
      <div class="row"><svg class="icon"><use href="#i-fax"/></svg>555-418-2056</div>
      <div class="row"><svg class="icon"><use href="#i-mail"/></svg>info@brightnest.com</div>
    </div>
  </div>
  <div class="band" style="top:109px"><span class="url" style="left:50px">WWW.BRIGHTNEST.COM</span><span class="chip" style="left:187px"></span></div>
</section>
<div class="label" style="left:174px;top:343px">Business Card Front</div>

<!-- Business card back -->
<section class="piece card card-back">
  <div class="mark on-dark" style="left:113px;top:30px">
    <div class="mark-square" style="width:34px;height:34px;margin-bottom:10px"></div>
    <div class="mark-name" style="font-size:9px">Brightnest Stays</div>
  </div>
  <div class="web">www.brightnest.com</div>
</section>
<div class="label" style="left:163px;top:504px">Business Card Back</div>

<!-- Letterhead -->
<section class="piece letterhead">
  <div class="mark" style="left:63px;top:27px">
    <div class="mark-square" style="width:26px;height:26px;margin-bottom:11px"></div>
    <div class="mark-name" style="font-size:7px">Brightnest Stays</div>
  </div>
  <div class="contact" style="left:223px;top:29px">
    <div>2140 Alder Crest Road</div>
    <div>Juneau, Alaska 99801</div>
    <div class="row"><svg class="icon"><use href="#i-phone"/></svg>555-210-4830</div>
    <div class="row"><svg class="icon"><use href="#i-mobile"/></svg>555-314-7729</div>
    <div class="row"><svg class="icon"><use href="#i-mail"/></svg>info@brightnest.com</div>
  </div>
  <div class="ghost-word" style="left:96px;top:205px;font-size:17px">Brightnest</div>
  <div class="letter">
    <div class="greeting">Dear Mr. Carter,</div>
    <p>Thank you for choosing to stay with us this season. We have prepared your suite with fresh linen, a stocked kitchen and a quiet workspace. Check-in opens at three in the afternoon and our team is on hand to help with any request during your visit.</p>
    <p>Your booking covers a flexible stay of up to thirty nights, with weekly cleaning and secure parking included. Should your plans change, simply let us know two days ahead and we will adjust the dates at no extra cost.</p>
    <p>We look forward to welcoming you and hope the space feels like home from the first evening.</p>
    <div class="closing">Sincerely,</div>
  </div>
  <div class="signature" role="img" aria-label="Handwritten signature in blue ink"></div>
  <div class="band" style="top:420px"><span class="url" style="left:102px">WWW.BRIGHTNEST.COM</span><span class="chip" style="left:263px"></span></div>
</section>
<div class="label" style="left:471px;top:504px">Letter Head</div>

<!-- Note pad large -->
<section class="piece pad-large">
  <div class="spiral-side"></div>
  <div class="mark" style="left:55px;top:30px">
    <div class="mark-square" style="width:22px;height:22px;margin-bottom:9px"></div>
    <div class="mark-name" style="font-size:6.6px">Brightnest Stays</div>
  </div>
  <div class="contact" style="left:197px;top:31px">
    <div>2140 Alder Crest Road</div>
    <div>Juneau, Alaska 99801</div>
    <div class="row"><svg class="icon"><use href="#i-phone"/></svg>555-210-4830</div>
    <div class="row"><svg class="icon"><use href="#i-mobile"/></svg>555-314-7729</div>
    <div class="row"><svg class="icon"><use href="#i-mail"/></svg>info@brightnest.com</div>
  </div>
  <div class="ghost-word" style="left:62px;top:222px;font-size:27px">Brightnest</div>
  <div class="ruled"></div>
  <div class="band" style="top:419px"><span class="url" style="left:76px">WWW.BRIGHTNEST.COM</span><span class="chip" style="left:236px"></span></div>
</section>
<div class="label" style="left:834px;top:505px">Note pad Large</div>

<!-- Note pad small -->
<section class="piece pad-small-cover">
  <div class="spiral-top"></div>
  <div class="mark on-dark" style="left:72px;top:72px">
    <div class="mark-square" style="width:32px;height:32px;margin-bottom:12px"></div>
    <div class="mark-name" style="font-size:8.6px">Brightnest Stays</div>
  </div>
  <div class="web">www.brightnest.com</div>
</section>
<section class="piece pad-small">
  <div class="spiral-top"></div>
  <div class="ghost-word" style="left:36px;top:95px;font-size:13px">Brightnest</div>
  <div class="ruled"></div>
  <div class="web">www.brightnest.com</div>
</section>
<div class="label" style="left:1082px;top:505px">Note pad Small</div>

<!-- Envelope back -->
<section class="piece env-back">
  <div class="flap">
    <div class="mark on-dark" style="left:217px;top:12px">
      <div class="mark-square" style="width:22px;height:22px;margin-bottom:5px"></div>
      <div class="mark-name" style="font-size:6px">Brightnest Stays</div>
    </div>
  </div>
</section>
<div class="label" style="left:261px;top:745px">Envelope Back</div>

<!-- Envelope front -->
<section class="piece env-front">
  <div class="mark" style="left:80px;top:22px">
    <div class="mark-square" style="width:28px;height:28px;margin-bottom:10px"></div>
    <div class="mark-name" style="font-size:8px">Brightnest Stays</div>
  </div>
  <div class="address" style="left:28px;top:82px">2140 Alder Crest Road<br>Juneau, Alaska 99801</div>
  <div class="band" style="top:170px"><span class="url" style="left:28px">WWW.BRIGHTNEST.COM</span><span class="chip" style="left:370px"></span></div>
</section>
<div class="label" style="left:262px;top:981px">Envelope Front</div>

<!-- Envelope A4 -->
<section class="piece env-tall env-a4">
  <svg class="flap" width="288" height="39" viewBox="0 0 288 39"><path d="M0 39 L5 14 Q8 0 22 0 H266 Q280 0 283 14 L288 39 Z" fill="var(--ink)"/></svg>
  <div class="body">
    <div class="mark" style="left:52px;top:17px">
      <div class="mark-square" style="width:27px;height:27px;margin-bottom:9px"></div>
      <div class="mark-name" style="font-size:8px">Brightnest Stays</div>
    </div>
    <div class="address" style="left:22px;top:71px;font-size:6.8px;line-height:9px">2140 Alder Crest Road<br>Juneau, Alaska 99801</div>
    <div class="ghost-word" style="left:74px;top:172px;font-size:22px">Brightnest</div>
    <div class="band" style="top:358px"><span class="url" style="left:29px">WWW.BRIGHTNEST.COM</span><span class="chip" style="left:237px"></span></div>
  </div>
</section>
<div class="label" style="left:686px;top:981px">Envelope A4</div>

<!-- Envelope A5 -->
<section class="piece env-tall env-a5">
  <svg class="flap" width="295" height="39" viewBox="0 0 295 39"><path d="M0 39 L5 14 Q8 0 22 0 H273 Q287 0 290 14 L295 39 Z" fill="var(--ink)"/></svg>
  <div class="body">
    <div class="mark" style="left:53px;top:19px">
      <div class="mark-square" style="width:27px;height:27px;margin-bottom:9px"></div>
      <div class="mark-name" style="font-size:8px">Brightnest Stays</div>
    </div>
    <div class="address" style="left:22px;top:73px;font-size:6.8px;line-height:9px">2140 Alder Crest Road<br>Juneau, Alaska 99801</div>
    <div class="ghost-word" style="left:78px;top:172px;font-size:22px">Brightnest</div>
    <div class="band" style="top:357px"><span class="url" style="left:34px">WWW.BRIGHTNEST.COM</span><span class="chip" style="left:245px"></span></div>
  </div>
</section>
<div class="label" style="left:1027px;top:981px">Envelope A5</div>
</body>
</html>
```